Photo Storage Service - Web Application

This is web design for a simple photo storage service.
There is a web page and on the left side is a list of folders and on the right side there are photo thumbnails. By pressing a photo thumbnail, they will see the full size (it's just a link to a different page).
This project is limited only to ONE page, which is the page with the folders list and the thumbnails. However it contains some features that I will try to list here:
- Name of the service: Teso Vault
- Location of account: http://username.tesovault.example
- Folder list: Show all folders belonging to the user. Because you have to be able to drag photos to a folder, they have to be visible and cannot be hidden behind a menu item etc.
- Thumbnails with photos (in the future also videos)
- Adjusted view with smaller thumbnails and less space for folder list (so it is possible to view a larger quantity of thumbnails)- Select multiple thumbnails with rectangle- Show that a thumbnail is selected (maybe bold border?)
- Simple mobile view, but no emphasis on the mobile view in this design project.
- Drag one or more selected photos to a folder
- Delete one or more selected photos
- Drag a folder to another folder
- Rename folder
- Delete folder
- Create folder
- Show progress when deleting/moving (because it calls for every photo, so if there are 100 photos, it will delete 1 by 1 and it will take about 10 seconds - you could show progress bar or equivalent)
Background information: This is for a photo storage service NOT intended for sharing photos, but intended to indefinitely store photos and for yourself to browse your own photos.
It is a design requirement that it loads extremely fast. So we need to limit as much as possible extra graphics that cannot be done by CSS and other external libraries.
(I know this is ONLY design and nothing to do with CSS or libraries, but I can assess from the design if it might be heavy to load when implemented)
I have attached a crude screenshot of the current design, just for your understanding. It should not match this design and you are not in any way supposed to FIT your design into this same style or structure.
Target Market(s)
Consumers
Number of Pages Required
1 page

```html
<!DOCTYPE html>
<html lang="en">
<head>
<meta charset="utf-8">
<title>Teso Vault – My Photos</title>
<link href="https://fonts.googleapis.com/css2?family=Open+Sans:wght@400;600;700&display=swap" rel="stylesheet">
<style>
:root{
  --white:#ffffff;
  --band:#f4f4f4;
  --search:#f7f7f7;
  --text-muted:#a6a6a6;
  --logo:#9a9a9a;
  --sidebar:#9b9b9b;
  --sidebar-active:#333333;
  --sidebar-text:#ffffff;
  --accent:#00b7e8;
  --menu:#1aa5d3;
  --menu-line:#4cbbe0;
  --note:#e01b1b;
}
*{box-sizing:border-box;margin:0;padding:0}
html,body{width:1200px;height:1200px;overflow:hidden;background:var(--white)}
body{font-family:"Open Sans",sans-serif}
.stage{position:relative;width:1216px;height:1216px;transform:scale(0.98684);transform-origin:0 0;overflow:hidden}
.brand{position:absolute;left:60px;top:26px;font-size:31px;font-weight:700;color:var(--logo);letter-spacing:-0.5px}
.search{position:absolute;left:775px;top:28px;width:460px;height:36px;border-radius:18px;background:var(--search);padding-left:20px;font-size:12px;line-height:36px;color:#c2c2c2}
.crumbs{position:absolute;left:0;top:90px;width:1216px;height:37px;background:var(--band);padding-left:60px;font-size:13px;line-height:37px;color:var(--text-muted)}
.folders{position:absolute;left:60px;top:160px;width:293px;height:971px;background:var(--sidebar);list-style:none}
.folder{height:37px;padding-left:38px;font-size:15px;line-height:37px;color:var(--sidebar-text)}
.folder--inbox{height:58px;line-height:60px}
.folder--active{position:relative;height:59px;line-height:59px;padding-left:27px;background:var(--sidebar-active);font-weight:700;margin-bottom:6px}
.dropzone{position:absolute;right:14px;top:15px;width:48px;height:30px;font-size:10px;font-weight:400;line-height:28px;text-align:center;color:#bdbdbd}
.dropzone svg{position:absolute;left:0;top:0}
.drag-cue{position:absolute;left:243px;top:257px;z-index:5}
.note{position:absolute;z-index:6;color:var(--note);font-size:16px;font-weight:600;white-space:nowrap}
.grid{position:absolute;left:384px;top:160px;z-index:1}
.tile{position:absolute;width:283px;height:236px}
.tile.faded::after{content:"";position:absolute;inset:0;background:rgba(255,255,255,.38)}
.tile.selected{outline:6px solid var(--accent);outline-offset:-6px}
.tile.selected .photo{position:absolute;inset:6px}
.photo{position:absolute;inset:0}
.check{z-index:3}
.menu{position:absolute;z-index:4;left:571px;top:343px;width:175px;background:var(--menu);list-style:none;box-shadow:0 2px 6px rgba(0,0,0,.2)}
.menu li{position:relative;height:35px;padding-left:20px;font-size:13px;font-weight:700;line-height:35px;color:var(--white);border-bottom:1px solid var(--menu-line)}
.menu li:last-child{border-bottom:none}
.menu svg{position:absolute;right:13px;top:9px}
</style>
</head>
<body>
<div class="stage">
  <header>
    <div class="brand">Teso Vault</div>
    <div class="search">Search image, category...</div>
  </header>
  <nav class="crumbs">My Photos /</nav>

  <ul class="folders">
    <li class="folder folder--inbox">Inbox</li>
    <li class="folder folder--active">Favourite Photos
      <span class="dropzone"><svg width="48" height="30"><path d="M10 1H1v8M38 1h9v8M10 29H1v-8M38 29h9v-8" fill="none" stroke="#bdbdbd" stroke-width="1.5"/></svg>Drag Here</span>
    </li>
    <li class="folder">A day in Oslo</li>
    <li class="folder">A your of Svendborg</li>
    <li class="folder">Alicante 2017</li>
    <li class="folder">Alicante after Christmas</li>
    <li class="folder">Bandarban</li>
    <li class="folder">Bird Lightly Garnished</li>
    <li class="folder">Brazil</li>
    <li class="folder">Days in Denmark - Christmas</li>
    <li class="folder">Mobile Uploads</li>
    <li class="folder">Random</li>
    <li class="folder">Recently Uploaded from Phone</li>
    <li class="folder">Sundarban</li>
    <li class="folder">Sylhet II</li>
    <li class="folder">Tea Garden</li>
    <li class="folder">Thailand 1</li>
    <li class="folder">Thailand 1</li>
    <li class="folder">Thailand 2018</li>
    <li class="folder">Timeline Photos</li>
    <li class="folder">USA</li>
    <li class="folder">UploadBag</li>
    <li class="folder">Vancouver</li>
    <li class="folder">Thumbnails</li>
    <li class="folder">Videos/Thumbnails</li>
  </ul>

  <div class="grid">
    <div class="tile selected" style="left:0;top:0"><div class="photo" role="img" aria-label="Looking up at tall office towers" style="background:linear-gradient(100deg,#e8eaec 0%,#b8bcc0 40%,#6b625c 60%,#c4c6c8 100%)"></div></div>
    <div class="tile selected" style="left:292px;top:0"><div class="photo" role="img" aria-label="Man on a railing overlooking misty hills" style="background:linear-gradient(180deg,#d8cfc2 0%,#a69c8c 40%,#2e3440 75%,#1c222c 100%)"></div></div>
    <div class="tile faded" style="left:584px;top:0"><div class="photo" role="img" aria-label="Dark blue leaves with water drops" style="background:radial-gradient(circle at 50% 50%,#4e7c86,#22333d)"></div></div>

    <div class="tile faded" style="left:0;top:245px"><div class="photo" role="img" aria-label="Foggy valley with pine forest" style="background:linear-gradient(180deg,#c9c2ac 0%,#a7a58a 55%,#6f7358 100%)"></div></div>
    <div class="tile selected" style="left:292px;top:245px"><div class="photo" role="img" aria-label="Snowy city street with a red stickered box" style="background:linear-gradient(90deg,#a12534 0%,#7d2a33 30%,#8e8e8e 60%,#c7c1bc 100%)"></div></div>
    <div class="tile selected" style="left:584px;top:245px"><div class="photo" role="img" aria-label="Silhouette of a person at a blue window" style="background:linear-gradient(90deg,#2a5d7e 0%,#3e7fa4 40%,#0f1a22 70%,#2a5a7a 100%)"></div></div>

    <div class="tile faded" style="left:0;top:490px"><div class="photo" role="img" aria-label="Hand holding small white flowers" style="background:linear-gradient(180deg,#c69a80 0%,#8d7c74 50%,#5a5e63 100%)"></div></div>
    <div class="tile faded" style="left:292px;top:490px"><div class="photo" role="img" aria-label="Snowy mountain under a starry sky" style="background:linear-gradient(180deg,#4a4f56 0%,#8a8d90 50%,#d0d0d0 100%)"></div></div>
    <div class="tile" style="left:584px;top:490px"><div class="photo" role="img" aria-label="City buildings against a blue sky" style="background:linear-gradient(180deg,#8fb6d4 0%,#7f8e96 40%,#6d5446 70%,#3a3a3a 100%)"></div></div>

    <div class="tile faded" style="left:0;top:735px"><div class="photo" role="img" aria-label="Person standing in a yellow walled alley" style="background:linear-gradient(90deg,#c7b22a 0%,#7d7566 30%,#6f6f6c 70%,#c2ad2c 100%)"></div></div>
    <div class="tile faded" style="left:292px;top:735px"><div class="photo" role="img" aria-label="Iced drink on a wooden table" style="background:linear-gradient(180deg,#d9d7d3 0%,#b8a48a 55%,#9c8062 100%)"></div></div>
    <div class="tile faded" style="left:584px;top:735px"><div class="photo" role="img" aria-label="White spiral staircase" style="background:radial-gradient(circle at 40% 45%,#5c6166,#bfc3c6 45%,#e8eaeb)"></div></div>

    <div class="tile faded" style="left:0;top:979px"><div class="photo" role="img" aria-label="Blue waterfall scene" style="background:linear-gradient(180deg,#3d6f9e,#a9c7df)"></div></div>
    <div class="tile faded" style="left:292px;top:979px"><div class="photo" role="img" aria-label="Pink backdrop" style="background:#e98a90"></div></div>
    <div class="tile faded" style="left:584px;top:979px"><div class="photo" role="img" aria-label="Laptop on a desk" style="background:linear-gradient(180deg,#d6d2cc,#9a9590)"></div></div>
  </div>

  <svg class="check" style="position:absolute;left:620px;top:172px" width="34" height="34"><rect x="2" y="2" width="30" height="30" rx="5" fill="#fff" stroke="#00b7e8" stroke-width="3"/><path d="M9 17l6 6 11-13" fill="none" stroke="#00b7e8" stroke-width="3.5"/></svg>
  <svg class="check" style="position:absolute;left:912px;top:172px" width="34" height="34"><rect x="2" y="2" width="30" height="30" rx="5" fill="#fff" stroke="#00b7e8" stroke-width="3"/><path d="M9 17l6 6 11-13" fill="none" stroke="#00b7e8" stroke-width="3.5"/></svg>
  <svg class="check" style="position:absolute;left:909px;top:419px" width="34" height="34"><rect x="2" y="2" width="30" height="30" rx="5" fill="#fff" stroke="#00b7e8" stroke-width="3"/><path d="M9 17l6 6 11-13" fill="none" stroke="#00b7e8" stroke-width="3.5"/></svg>
  <svg class="check" style="position:absolute;left:1200px;top:419px" width="34" height="34"><rect x="2" y="2" width="30" height="30" rx="5" fill="#fff" stroke="#00b7e8" stroke-width="3"/><path d="M9 17l6 6 11-13" fill="none" stroke="#00b7e8" stroke-width="3.5"/></svg>

  <ul class="menu">
    <li>Delete Selected<svg width="14" height="16"><path d="M2 4h10M5 4V2h4v2M3 4l1 11h6l1-11M6 7v5M8 7v5" fill="none" stroke="#fff" stroke-width="1.3"/></svg></li>
    <li>Copy Selected<svg width="17" height="17"><rect x="1" y="1" width="9" height="11" fill="none" stroke="#fff" stroke-width="1.3"/><rect x="6" y="5" width="9" height="11" fill="#1aa5d3" stroke="#fff" stroke-width="1.3"/><path d="M8 9h5M8 12h5" stroke="#fff" stroke-width="1.2"/></svg></li>
    <li>Cut Selected<svg width="18" height="18"><circle cx="4" cy="13" r="2.5" fill="none" stroke="#fff" stroke-width="1.3"/><circle cx="13" cy="14" r="2.5" fill="none" stroke="#fff" stroke-width="1.3"/><path d="M6 11l10-9M11 12L6 2" stroke="#fff" stroke-width="1.3"/></svg></li>
  </ul>

  <svg class="drag-cue" width="56" height="52" viewBox="0 0 56 52">
    <rect x="13" y="4" width="28" height="28" rx="7" fill="none" stroke="#00b7e8" stroke-width="3"/>
    <rect x="20" y="10" width="28" height="28" rx="7" fill="#e6f7fc" stroke="#00b7e8" stroke-width="3"/>
    <path d="M3 26v22l5-5 4 8 3-1-4-8h7z" fill="#fff" stroke="#555" stroke-width="1.2"/>
  </svg>
  <div class="note" style="left:265px;top:322px">Drag selected Image</div>
  <div class="note" style="left:494px;top:471px">Left Click Popup</div>
</div>
</body>
</html>
```